Visiting Card / Envelope design / Letterhead for MARLOW

I need for our company a new

Visiting Card / Envelope design / Letterhead

please see enclosed logo:

Use any US address and the company's name is MARLOW GENERAL CONSTRUCTION INC.

BE CREATIVE, not usual ))

```html
<!DOCTYPE html>
<html lang="en">
<head>
<meta charset="utf-8">
<title>Marlow General Construction Inc. – Stationery</title>
<link rel="stylesheet" href="https://fonts.googleapis.com/css2?family=Jost:wght@300;400&display=swap">
<style>
  :root {
    --bg: #e6e6e8;
    --paper: #ffffff;
    --navy: #262a6b;
    --navy-soft: #3d3f74;
    --blue: #3d7ee0;
    --grid-blue: #3a74d6;
    --red: #b0344f;
    --rose: #e8b7c2;
    --lilac: #b5b7cc;
    --ink: #2a2d5a;
  }
  * { box-sizing: border-box; margin: 0; padding: 0; }
  html, body { width: 1200px; height: 1140px; overflow: hidden; }
  body { background: var(--bg); font-family: "Jost", Arial, sans-serif; font-weight: 300; color: var(--ink); position: relative; }

  .card, .envelope { position: absolute; background: var(--paper); overflow: hidden; }

  /* Business card front */
  .card-front { left: 457px; top: 123px; width: 347px; height: 205px; }
  .card-front .decor { position: absolute; inset: 0; }
  .card-front .wordmark { position: absolute; left: 10px; top: 8px; }
  .wordmark .name { color: var(--navy); font-size: 30px; letter-spacing: 0.5px; line-height: 1; }
  .wordmark .tagline { color: var(--red); font-size: 12.5px; letter-spacing: 0.3px; margin-top: 3px; }
  .card-front .mark { position: absolute; right: 16px; top: 22px; display: flex; align-items: center; gap: 5px; }
  .mark .square { width: 12px; height: 12px; background: var(--red); }
  .mark .label { color: var(--navy); font-size: 17px; font-weight: 400; }
  .contact { position: absolute; font-size: 11.5px; line-height: 17px; color: var(--ink); white-space: nowrap; }
  .card-front .contact { left: 10px; top: 104px; font-size: 10.5px; line-height: 16px; }

  /* Business card back */
  .card-back { left: 463px; top: 361px; width: 334px; height: 206px; display: flex; }
  .card-back .pattern { width: 104px; height: 100%; background: var(--grid-blue); }
  .card-back .pattern:last-child { width: 103px; }
  .card-back .center { flex: 1; display: flex; flex-direction: column; align-items: center; justify-content: center; gap: 4px; }
  .card-back .center .label { color: var(--navy); font-size: 24px; font-weight: 400; line-height: 1; }
  .card-back .center .sub { color: var(--navy); font-size: 7.5px; letter-spacing: 0.2px; }
  .card-back .center .square { width: 12px; height: 12px; background: var(--red); }

  /* Envelope */
  .envelope { left: 287px; top: 703px; width: 682px; height: 301px; border-radius: 5px; }
  .envelope .decor { position: absolute; inset: 0; }
  .envelope .wordmark { position: absolute; left: 23px; top: 14px; }
  .envelope .wordmark .name { font-size: 40px; color: var(--navy); }
  .envelope .wordmark .tagline { font-size: 17px; margin-top: 2px; letter-spacing: 0.5px; }
  .envelope .mark { position: absolute; left: 511px; top: 71px; width: 109px; height: 117px; display: flex; flex-direction: column; align-items: center; justify-content: center; gap: 4px; }
  .envelope .mark .label { font-size: 21px; }
  .envelope .mark .sub { color: var(--navy); font-size: 7px; }
  .envelope .contact { left: 23px; top: 167px; font-size: 12.5px; line-height: 17px; }
</style>
</head>
<body>

  <section class="card card-front" aria-label="Business card front">
    <svg class="decor" viewBox="0 0 347 205" width="347" height="205" aria-hidden="true">
      <polyline points="205,205 264,98 347,86" fill="none" stroke="var(--rose)" stroke-width="5"/>
      <g fill="var(--lilac)">
        <rect x="285" y="95" width="20" height="20" transform="rotate(45 295 105)"/>
        <rect x="266" y="120" width="20" height="20" transform="rotate(45 276 130)"/>
        <rect x="304" y="120" width="20" height="20" transform="rotate(45 314 130)"/>
        <rect x="285" y="145" width="20" height="20" transform="rotate(45 295 155)"/>
      </g>
    </svg>
    <div class="wordmark">
      <div class="name">MARLOW</div>
      <div class="tagline">GENERAL CONSTRUCTION INC</div>
    </div>
    <div class="mark"><span class="square"></span><span class="label">MARLOW</span></div>
    <div class="contact">
      <p>Dana Whitfield&nbsp; 218 Alder Ridge Rd. California</p>
      <p>tel.+1 555 204 718</p>
      <p>hello@marlowbuilds.com</p>
    </div>
  </section>

  <section class="card card-back" aria-label="Business card back">
    <div class="pattern" role="img" aria-label="Blue tiled grid pattern"></div>
    <div class="center">
      <span class="square"></span>
      <span class="label">MARLOW</span>
      <span class="sub">GENERAL CONSTRUCTION INC</span>
    </div>
    <div class="pattern" role="img" aria-label="Blue tiled grid pattern"></div>
  </section>

  <section class="envelope" aria-label="Envelope">
    <svg class="decor" viewBox="0 0 682 301" width="682" height="301" aria-hidden="true">
      <path d="M0 0 H682 V62 Q660 70 600 76 L420 90 Q380 92 340 93 H0 Z" fill="var(--blue)"/>
      <rect x="511" y="0" width="109" height="71" fill="var(--navy)"/>
      <rect x="511" y="188" width="109" height="113" fill="var(--navy-soft)"/>
      <polyline points="401,0 427,212 0,295" fill="none" stroke="var(--red)" stroke-width="5"/>
      <circle cx="348" cy="102" r="21" fill="#111"/>
    </svg>
    <div class="wordmark">
      <div class="name">MARLOW</div>
      <div class="tagline">GENERAL CONSTRUCTION INC</div>
    </div>
    <div class="mark">
      <span class="square"></span>
      <span class="label">MARLOW</span>
      <span class="sub">GENERAL CONSTRUCTION INC</span>
    </div>
    <div class="contact">
      <p>Dana Whitfield&nbsp; 218 Alder Ridge Rd. California</p>
      <p>tel.+1 555 204 718</p>
      <p>hello@marlowbuilds.com</p>
    </div>
  </section>

</body>
</html>
```